seeking a modern Business Card design for Roof Plumbering Business

wexcombe roof plumbing is a local metal re-roof and new construction specialist. We are seeking a modern business card to assist with networking within the industry. Our services are predominantly the installation of metal roofs on new houses, however we also do re-roofs when an existing roof needs replacing. We service both residential and commercial properties. Please include the below details on the card:
Name: Owen Wexcombe
Phone: 0471 385 962
Email: owenwexcomberoofing@mailnest.example

Residential & Commercial
Re-roof & New Construction
Fully Insured

I have uploaded our business logo, which we think would suit a black background. Please use all lower case for business name.
Cheers
Updates

Hey Guys, As requested I've uploaded a Pdf version of my logo. Hopefully this help. Thanks

Industry/Entity Type

Business

Contact Information for Business Card

Name: Owen Wexcombe
Phone: 0471 385 962

Residential & Commercial
Fully Insured

Font styles to use
Serif
Sans Serif

Requirements
Must have
• Name must be all lower case "wexcombe roof plumbing"
Nice to have
• Stick with Logo Colours

```html
<!DOCTYPE html>
<html lang="en">
<head>
<meta charset="utf-8">
<title>wexcombe roof plumbing – business card</title>
<link rel="stylesheet" href="https://fonts.googleapis.com/css2?family=Montserrat:wght@400;500;600&display=swap">
<style>
  :root {
    --page-bg: #d8d3cb;
    --card-black: #0b0b0c;
    --card-black-soft: #1c1c1e;
    --brand-blue: #27b4dc;
    --band-blue: #2ab6df;
    --band-blue-deep: #1e9fc6;
    --rule-grey: #8c8f93;
    --ink-dark: #101214;
  }
  * { margin: 0; padding: 0; box-sizing: border-box; }
  html, body {
    width: 1200px;
    height: 1022px;
    overflow: hidden;
    background: var(--page-bg);
    font-family: "Montserrat", Arial, sans-serif;
  }
  .canvas {
    position: relative;
    width: 1200px;
    height: 1022px;
  }
  .business-card {
    position: absolute;
    left: 100px;
    top: 225px;
    width: 1000px;
    height: 572px;
    border-radius: 26px;
    overflow: hidden;
    background: linear-gradient(160deg, var(--card-black-soft) 0%, var(--card-black) 55%);
    box-shadow: 0 18px 40px rgba(0, 0, 0, 0.28);
  }
  .brand-lockup {
    position: absolute;
    left: 70px;
    top: 130px;
    display: flex;
    align-items: center;
    gap: 16px;
  }
  .brand-mark {
    width: 22px;
    height: 22px;
    background: var(--brand-blue);
  }
  .brand-name {
    color: var(--brand-blue);
    font-weight: 500;
    font-size: 34px;
    letter-spacing: 1px;
    line-height: 1;
  }
  .company-title {
    position: absolute;
    left: 70px;
    top: 300px;
    color: var(--brand-blue);
    font-weight: 500;
    font-size: 26px;
    letter-spacing: 2px;
    text-transform: uppercase;
  }
  .band-rule {
    position: absolute;
    left: 0;
    right: 0;
    top: 354px;
    height: 8px;
    background: var(--rule-grey);
  }
  .contact-band {
    position: absolute;
    left: 0;
    right: 0;
    top: 362px;
    bottom: 0;
    background: linear-gradient(180deg, var(--band-blue) 0%, var(--band-blue-deep) 100%);
    color: var(--ink-dark);
  }
  .contact-person {
    position: absolute;
    left: 70px;
    top: 38px;
  }
  .person-name {
    font-weight: 600;
    font-size: 34px;
    letter-spacing: 1.5px;
    text-transform: uppercase;
    margin-bottom: 18px;
  }
  .contact-line {
    display: flex;
    align-items: center;
    gap: 12px;
    font-weight: 400;
    font-size: 19px;
    letter-spacing: 0.5px;
    line-height: 1.4;
  }
  .contact-icon {
    width: 16px;
    height: 16px;
    flex: none;
  }
  .service-list {
    position: absolute;
    right: 50px;
    top: 40px;
    list-style: none;
    text-align: right;
    font-weight: 400;
    font-size: 21px;
    letter-spacing: 0.5px;
    line-height: 1.45;
  }
</style>
</head>
<body>
<main class="canvas">
  <article class="business-card">
    <div class="brand-lockup">
      <span class="brand-mark" aria-hidden="true"></span>
      <span class="brand-name">wexcombe roof plumbing</span>
    </div>

    <p class="company-title">Wexcombe Roof Plumbing</p>

    <div class="band-rule"></div>

    <section class="contact-band">
      <div class="contact-person">
        <h1 class="person-name">Owen Wexcombe</h1>
        <p class="contact-line">
          <svg class="contact-icon" viewBox="0 0 16 16" aria-hidden="true">
            <path d="M3.5 1.5 L6 1.5 L7 5 L5.3 6.2 C6.2 8 7.9 9.8 9.8 10.7 L11 9 L14.5 10 L14.5 12.5 C14.5 13.6 13.6 14.5 12.5 14.5 C6.5 14.5 1.5 9.5 1.5 3.5 C1.5 2.4 2.4 1.5 3.5 1.5 Z" fill="none" stroke="#101214" stroke-width="1.4"/>
          </svg>
          0471 385 962
        </p>
        <p class="contact-line">
          <svg class="contact-icon" viewBox="0 0 16 16" aria-hidden="true">
            <rect x="1.5" y="3.5" width="13" height="9" fill="none" stroke="#101214" stroke-width="1.4"/>
            <path d="M1.5 3.5 L8 9 L14.5 3.5" fill="none" stroke="#101214" stroke-width="1.4"/>
          </svg>
          owenwexcomberoofing@mailnest.example
        </p>
      </div>

      <ul class="service-list">
        <li>Residential &amp; Commercial</li>
        <li>Re-roof &amp; New Construction</li>
        <li>Fully Insured</li>
      </ul>
    </section>
  </article>
</main>
</body>
</html>
```